Broschüre im Bereich Steuerberatung
Zielgruppe
Steuerberatung
Aufgabenstellung
Die Seite 1 wäre eigentlich fertig, natürlich bin ich offen für Optimierungen. Die weiteren fünf Seiten gilt es noch zu gestalten:
Seite 1
Buchhaltung
Lohnwesen
Steuern
Firmengründung
Kontakt

```html
<!DOCTYPE html>
<html lang="de">
<head>
<meta charset="utf-8">
<title>Broschüre Berner Treuhand</title>
<link href="https://fonts.googleapis.com/css2?family=Barlow+Condensed:wght@500&family=Jost:ital,wght@0,400;0,500;0,700;1,400&family=Source+Serif+4:ital,wght@0,400;1,400&display=swap" rel="stylesheet">
<style>
:root{
  --bg:#dcdcd4;
  --paper:#ffffff;
  --navy:#1e3f7a;
  --orange:#e8632a;
  --green:#9fb53b;
  --ink:#3a3a3a;
}
*{margin:0;padding:0;box-sizing:border-box}
html,body{width:1114px;height:1200px;overflow:hidden;background:var(--bg)}
body{position:relative;font-family:"Jost",sans-serif;color:var(--ink)}
.page{position:absolute;width:469px;height:331px;background:var(--paper)}
.p1{left:60px;top:58px}.p2{left:573px;top:58px}
.p3{left:60px;top:423px}.p4{left:573px;top:423px}
.p5{left:60px;top:796px}.p6{left:573px;top:796px}
.abs{position:absolute}
.kicker{position:absolute;left:20px;top:43px;font-family:"Barlow Condensed",sans-serif;font-weight:500;font-size:14px;letter-spacing:2.6px;color:var(--navy);white-space:nowrap;line-height:16px}
.kicker .sep{display:inline-block;width:5px;height:5px;background:var(--orange);margin:0 5px 0 2px;vertical-align:middle;position:relative;top:-1px}
.photo{position:absolute;left:20px;top:67px;width:223px;height:223px;overflow:hidden}
.ph-city{background:linear-gradient(160deg,#b28aa4 0%,#7f8fa8 40%,#6f8a6c 70%,#8a8676 100%)}
.ph-trees{background:linear-gradient(135deg,#e19a7a 0%,#c7a04e 35%,#8aa23e 60%,#4f7a5a 85%,#3f6fa8 100%)}
.ph-glass{background:linear-gradient(120deg,#b88a45 0%,#8a9a3f 40%,#5a87a8 75%,#3e6c9b 100%)}
.ph-street{background:linear-gradient(180deg,#c49fa8 0%,#a39596 35%,#6f8c60 65%,#8d8a85 100%)}
.ph-river{background:linear-gradient(165deg,#c6a0a2 0%,#a48a73 40%,#7d7a45 70%,#6b5a55 100%)}
.big{position:absolute;right:10px;top:10px;font-family:"Source Serif 4",serif;font-size:46px;line-height:0.9;color:#fff;text-align:right}
.url-on{position:absolute;right:20px;bottom:13px;font-size:7px;font-weight:700;color:var(--orange)}
.col{position:absolute;left:253px;width:198px}
h2.title{font-size:7.4px;font-weight:700;color:var(--navy);line-height:1.3}
.lead{font-size:5.6px;font-weight:700;color:var(--orange);margin-top:3px;line-height:1.35}
p,li{font-size:4.6px;line-height:1.45;color:var(--ink)}
p+p{margin-top:4px}
h3{font-size:7px;font-weight:700;color:var(--navy);letter-spacing:.2px;margin-bottom:1px}
.txt{position:absolute;width:91px}
.portrait{position:absolute;left:357px;top:89px;width:94px;height:66px;background:linear-gradient(180deg,#eef0f0,#d9dcdc)}
.badge{position:absolute;width:58px;height:58px;border-radius:50%;background:var(--green);border:2px solid #fff;box-shadow:0 0 0 1px var(--green)}
.badge svg{position:absolute;left:13px;top:13px}
.link{position:absolute;font-size:5.6px;font-weight:700;color:var(--orange);line-height:1.4}
.arrow-item{position:absolute;left:357px;width:95px;padding-left:15px;font-size:5px;font-weight:700;color:var(--navy);line-height:1.35}
.arrow-item svg{position:absolute;left:0;top:0}
.steps{position:absolute;left:410px;top:104px;width:40px;text-align:center}
.step{margin-bottom:9px;font-size:5px;font-weight:700;color:var(--navy);line-height:1.2}
.step svg{display:block;margin:0 auto 2px}
.serv{position:absolute;left:253px;top:177px;font-size:7.4px;font-weight:700;color:var(--navy);line-height:1.3}
.serv em{font-family:"Source Serif 4",serif;font-weight:400}
.pack{position:absolute;left:257px;top:205px;width:110px}
.pack h4{font-size:5.6px;font-weight:700;color:var(--navy);letter-spacing:.4px;text-align:center}
.pack .price{font-size:5.6px;font-weight:700;color:var(--orange);text-align:center;margin-bottom:4px}
.pack ul{list-style:none}
.pack li{position:relative;padding-left:8px;font-size:4.6px;margin-bottom:2.5px}
.pack li svg{position:absolute;left:0;top:1px}
.pack .note{font-size:3.6px;padding-left:8px;font-style:italic}
.brandname{position:absolute;left:378px;top:228px;font-size:13px;font-weight:700;color:var(--navy)}
.brandname .dot{display:inline-block;width:7px;height:7px;border-radius:50%;background:var(--orange);margin-left:3px}
.btn{position:absolute;left:253px;top:274px;width:108px;height:15px;border-radius:8px;background:var(--green);color:#fff;font-size:6.4px;font-weight:700;letter-spacing:1px;text-align:center;line-height:15px}
.contact-line{font-size:5px;margin-bottom:3px;display:flex;align-items:center;gap:5px}
.addr h3{margin-bottom:2px}
.addr p{font-size:4.8px;line-height:1.55}
.map{position:absolute;top:164px;width:165px;height:126px;background:linear-gradient(135deg,#f3f4f7,#e6e9f0)}
</style>
</head>
<body>

<!-- Seite 1 -->
<section class="page p1">
  <div class="kicker">STEUERN<span class="sep"></span>MEHRWERT<span class="sep"></span>TREUHAND<span class="sep"></span></div>
  <div class="photo ph-city" role="img" aria-label="Foto einer Stadtstrasse mit Hochhäusern und Bäumen">
    <div class="big">berner</div>
    <div class="url-on">bernertreuhand.ch</div>
  </div>
  <div class="col" style="top:65px">
    <h2 class="title">Zuverlässig und partnerschaftlich:<br>Ihre massgeschneiderten Treuhand-Lösungen</h2>
  </div>
  <div class="txt" style="left:253px;top:90px">
    <p>Sie möchten Ihre Steuern, Ihre Buchhaltung oder Ihr Lohnwesen in verlässliche Hände geben? Sie legen Wert auf eine persönliche Betreuung mit gleichbleibendem Ansprechpartner, auf individuelle Strategien und auf ein angenehmes Miteinander?</p>
    <p>Dann freue ich mich auf Ihre Kontaktaufnahme.</p>
  </div>
  <div class="portrait" role="img" aria-label="Porträtfoto der Inhaberin"></div>
  <div class="txt" style="left:253px;top:178px">
    <h3>BUCHHALTUNG</h3>
    <p>Buchhaltung ist komplex und aufwendig – das kostet Unternehmer viel Zeit, die sie anderswo wertschöpfend einsetzen könnten. Mithilfe moderner Hilfsmittel und bewährter Prozesse entlaste ich Sie zuverlässig und zum Fixpreis.</p>
  </div>
  <div class="txt" style="left:357px;top:178px">
    <h3>STEUERERKLÄRUNG</h3>
    <p>Jeder möchte seine Steuerlast optimieren, nur wenige setzen sich aktiv damit auseinander. Denn das kostet Zeit und verlangt nach umfangreichem Wissen. Vertrauen Sie mir Ihre Steuererklärungen an – und holen Sie sich zurück, was Ihnen zusteht.</p>
  </div>
  <div class="txt" style="left:253px;top:241px">
    <h3>LOHNWESEN</h3>
    <p>Entscheiden Sie selbst, in welcher Form Sie auf meine Expertise zugreifen, um sich beim Thema Lohnbuchhaltung zu entlasten.</p>
  </div>
  <div class="txt" style="left:357px;top:241px">
    <h3>FIRMENGRÜNDUNG</h3>
    <p>Gründen Sie Ihre Schweizer Gesellschaft schnell und sicher. Mit meiner langjährigen Erfahrung, meinem Wissen und meiner Zusammenarbeit mit einem versierten Notar unterstütze ich Sie zuverlässig – auch über Ihre Gründung hinaus.</p>
  </div>
</section>

<!-- Seite 2 -->
<section class="page p2">
  <div class="kicker">ADDITION<span class="sep"></span>SUBTRAKTION<span class="sep"></span>ERFOLG<span class="sep"></span></div>
  <div class="photo ph-trees" role="img" aria-label="Foto von Baumkronen vor Hochhausfassaden">
    <div class="big" style="top:14px">buch-<br>haltung</div>
  </div>
  <div class="badge" style="left:214px;top:238px">
    <svg width="28" height="28" viewBox="0 0 28 28" fill="none" stroke="#fff" stroke-width="1.6"><rect x="1" y="1" width="26" height="26" rx="2"/><path d="M5 8h6M17 5l5 5M22 5l-5 5M5 19h6M8 16v6M17 17h5M17 21h5"/></svg>
  </div>
  <div class="col" style="top:65px">
    <h2 class="title">Buchhaltung kostet Sie viel Zeit<br>– Ich gebe Sie Ihnen zurück</h2>
    <div class="lead">Ich übernehme Ihre Buchhaltung –<br>akribisch, verlässlich, verantwortungsvoll</div>
  </div>
  <div class="txt" style="left:253px;top:114px">
    <p>Unternehmer zählen die Buchhaltung in der Regel nicht zu ihren Leidenschaften.</p>
    <p>Und dennoch ist eine ordentliche Buchhaltung das Rückgrat eines jeden erfolgreichen Betriebs. Es ergibt also durchaus Sinn, hierfür ausreichend Ressourcen bereitzustellen – jedoch nicht die eigenen.</p>
    <p>Wenn Sie selbst oder Ihre Mitarbeiter sich um dieses komplexe „Pflichtthema“ kümmern, bleiben andere, wertschöpfende Tätigkeiten auf der Strecke: neue Kunden akquirieren, Produkte weiterentwickeln, Services ausbauen usw.</p>
  </div>
  <div class="txt" style="left:357px;top:114px">
    <p>Die Folge: Es kommt zu unnötigem Mehraufwand und die Entwicklung Ihres Unternehmens schreitet langsamer voran als geplant.</p>
    <p>Beides ist unschön – und beides lässt sich leicht vermeiden. Nutzen Sie Ihre wertvolle Zeit lieber gewinnbringend und überlassen Sie Ihre Buchhaltung einem Profi.</p>
    <p>Mit viel Erfahrung, Wissen und Leidenschaft kümmere ich mich um Ihre Geschäftsvorfälle, während Ihr Team sich auf Ihre Kerntätigkeit fokussiert.</p>
  </div>
  <div class="link" style="left:284px;top:261px">Mit individuellem Preisrechner auf:<br>www.bernertreuhand.ch/treuhand/buchhaltung</div>
</section>

<!-- Seite 3 -->
<section class="page p3">
  <div class="kicker">IHRE ZUKUNFT<span class="sep"></span>MEHR<span class="sep"></span>LOHN<span class="sep"></span></div>
  <div class="photo ph-glass" role="img" aria-label="Foto einer Glasfassade mit Bäumen">
    <div class="big" style="top:12px">lohn-<br>wesen</div>
  </div>
  <div class="col" style="top:65px">
    <h2 class="title">Lohnbuchhaltung ohne Stress:<br>So gewinnen Sie mehr Zeit</h2>
    <div class="lead">Ich erledige Ihr Lohnwesen – präzise, sicher, zuverlässig</div>
  </div>
  <div class="txt" style="left:253px;top:110px">
    <p>Sicherlich stimmen Sie mir zu, wenn ich das Personalwesen und die Salär­administration zu den sensiblen Bereichen Ihres Unternehmens zähle. Schliesslich erwarten Ihre Mitarbeiter, dass ihre Gehälter pünktlich auf dem Konto eingehen.</p>
    <p>Doch die Lohnbuchhaltung ist komplex und daher zeitaufwendig – sie bindet wertvolle Ressourcen, die Ihnen für andere, wertschöpfende Tätigkeiten fehlen.</p>
    <p>Holen Sie sich die Zeit zurück und legen Sie Ihre Lohnbuchhaltung in meine Hände. Dabei haben Sie die Wahl zwischen Optimierung und Outsourcing:</p>
  </div>
  <div class="arrow-item" style="top:106px">
    <svg width="10" height="10" viewBox="0 0 10 10"><circle cx="5" cy="5" r="5" fill="var(--orange)"/><path d="M2.5 5h4.5M5 3l2 2-2 2" stroke="#fff" stroke-width="1" fill="none"/></svg>
    Sie übernehmen die vorbereitenden Arbeiten, während ich mich um die Umsetzung kümmere. So optimieren wir gemeinsam Ihre Vorgänge und entlasten Ihre interne Buchhaltung.
  </div>
  <div class="arrow-item" style="top:159px">
    <svg width="10" height="10" viewBox="0 0 10 10"><circle cx="5" cy="5" r="5" fill="var(--orange)"/><path d="M2.5 5h4.5M5 3l2 2-2 2" stroke="#fff" stroke-width="1" fill="none"/></svg>
    Sie lagern Ihre Lohnbuchhaltung an mich aus. Insbesondere kleine und mittlere Unternehmen profitieren vom Outsourcing immens, da sie sich von diesem Thema komplett befreien.
  </div>
</section>

<!-- Seite 4 -->
<section class="page p4">
  <div class="kicker">ERFOLG LÄSST SICH STEUERN<span class="sep"></span></div>
  <div class="photo ph-street" role="img" aria-label="Foto einer von Bäumen gesäumten Stadtstrasse">
    <div class="big" style="top:14px">steuern</div>
  </div>
  <div class="badge" style="left:214px;top:238px">
    <svg width="28" height="28" viewBox="0 0 28 28" fill="none" stroke="#fff" stroke-width="1.6"><rect x="1" y="1" width="26" height="26" rx="2"/><path d="M5 8h6M17 5l5 5M22 5l-5 5M5 19h6M8 16v6M17 17h5M17 21h5"/></svg>
  </div>
  <div class="col" style="top:65px">
    <h2 class="title">Professionell und transparent:<br>Ihre Steuererklärung und Steuerberatung</h2>
    <div class="lead">Ich kümmere mich persönlich um Ihre Steuerangelegenheiten</div>
  </div>
  <div class="txt" style="left:253px;top:110px;width:130px">
    <p>Steuern sind ein sensibles Thema – schliesslich geht es um Ihr Geld. Setzen Sie gleich auf professionelle Unterstützung: Vermeiden Sie teure Fehler, sparen Sie viel Zeit und schonen Sie Ihre Nerven.</p>
    <h3 style="margin-top:6px">FÜR PRIVATPERSONEN</h3>
    <p>Weshalb ich mir viel Zeit für Sie nehme und Sie individuell betreue? Weil wir mit Konzepten „von der Stange“ bei Ihrer Steuererklärung nicht weit kommen.</p>
    <p>Hingegen habe ich die Abläufe rund um Ihre Steuerberatung standardisiert – um es Ihnen einfach zu machen: Wir tauschen uns per E-Mail, Telefon, Videocall oder per Post aus. So erhalten Sie schnelle Ergebnisse und sparen sich Weg und Kosten für einen persönlichen Termin.</p>
  </div>
  <div class="link" style="left:281px;top:241px">Mit individuellem Preisrechner auf:<br>www.bernertreuhand.ch/steuererklaerung</div>
  <div class="steps">
    <div class="step"><svg width="18" height="18" viewBox="0 0 18 18" fill="none" stroke="var(--navy)" stroke-width="1"><rect x="2" y="2" width="11" height="14"/><path d="M4 6h6M4 9h6M4 12h4M10 13l6-8"/></svg>Checkliste ausfüllen</div>
    <div class="step"><svg width="18" height="18" viewBox="0 0 18 18" fill="none" stroke="var(--orange)" stroke-width="1"><rect x="4" y="2" width="10" height="11"/><path d="M6 5h6M6 8h6M2 13h14v3H2z"/></svg>Unterlagen bereitstellen</div>
    <div class="step"><svg width="18" height="14" viewBox="0 0 18 14" fill="none" stroke="var(--orange)" stroke-width="1"><rect x="1" y="2" width="16" height="10"/><path d="M1 2l8 6 8-6"/></svg>Unterlagen übergeben</div>
    <div class="step"><svg width="16" height="18" viewBox="0 0 16 18" fill="none" stroke="var(--navy)" stroke-width="1"><rect x="2" y="1" width="12" height="16"/><path d="M4 8h8M4 11h8M4 14h5"/><text x="3.5" y="6" font-size="4" font-family="Jost,sans-serif" fill="var(--navy)" stroke="none">TAX</text></svg>Meine Arbeit</div>
    <div class="step"><svg width="16" height="18" viewBox="0 0 16 18" fill="none" stroke="var(--orange)" stroke-width="1"><path d="M2 1h8l4 4v12H2z"/><path d="M8 14V7M5 10l3-3 3 3"/></svg>Unterschreiben + Abgeben</div>
  </div>
</section>

<!-- Seite 5 -->
<section class="page p5">
  <div class="kicker">DON'T DREAM IT.<span class="sep"></span>DO IT!<span class="sep"></span></div>
  <div class="photo ph-river" role="img" aria-label="Foto einer Uferpromenade mit Bäumen und Velos">
    <div class="big" style="top:12px">firmen-<br>gründung</div>
  </div>
  <div class="col" style="top:65px">
    <h2 class="title">Berner Treuhand:<br>Professionelle Unternehmensgründung mit System</h2>
    <div class="lead">Berner Treuhand - Ihr kompetenter Partner</div>
  </div>
  <div class="txt" style="left:253px;top:107px">
    <p>Die Unternehmensgründung gehört zu den emotionalsten Erlebnissen in der Karriere. Gut, wenn man hierbei einen verlässlichen Partner hat, der einen kühlen Kopf bewahrt und sich bis ins Detail mit sämtlichen Anforderungen auskennt.</p>
  </div>
  <div class="txt" style="left:357px;top:107px">
    <p>Schon seit mehr als 13 Jahren unterstütze ich Start-ups auf ihrem Weg an die Spitze – vom ersten Tag an rund um die Gründung und danach bei der Buchhaltung, im Lohnwesen und bei den Steuern.</p>
  </div>
  <div class="serv">Kompetenter Service. <em>Komplett ohne<br>persönlichen Notartermin.</em></div>
  <div class="pack">
    <h4>FULLSERVICE-PAKET GRÜNDUNG</h4>
    <div class="price">CHF 750.-</div>
    <ul>
      <li><svg width="5" height="5" viewBox="0 0 5 5"><path d="M0.5 2.5l1.5 1.5 2.5-3.5" stroke="var(--orange)" fill="none" stroke-width="0.9"/></svg>Telefonische Beratung</li>
      <li><svg width="5" height="5" viewBox="0 0 5 5"><path d="M0.5 2.5l1.5 1.5 2.5-3.5" stroke="var(--orange)" fill="none" stroke-width="0.9"/></svg>Erstellen der Gründungsdokumente</li>
      <li><svg width="5" height="5" viewBox="0 0 5 5"><path d="M0.5 2.5l1.5 1.5 2.5-3.5" stroke="var(--orange)" fill="none" stroke-width="0.9"/></svg>Vertretung beim Notar durch Vollmacht</li>
      <li><svg width="5" height="5" viewBox="0 0 5 5"><path d="M0.5 2.5l1.5 1.5 2.5-3.5" stroke="var(--orange)" fill="none" stroke-width="0.9"/></svg>Anmeldung beim Handelsregisteramt</li>
    </ul>
    <div class="note">exkl. HR-Gebühren</div>
  </div>
  <div class="brandname">Berner<span class="dot"></span></div>
  <div class="btn">JETZT GRÜNDEN</div>
</section>

<!-- Seite 6 -->
<section class="page p6">
  <div class="col" style="left:20px;top:65px">
    <h2 class="title">Zuverlässig und partnerschaftlich:<br>Ihre massgeschneiderten Treuhand-Lösungen</h2>
    <div class="lead">Sie haben noch Fragen? Rufen Sie uns an oder senden<br>Sie uns eine Mail, wir helfen Ihnen gerne weiter.</div>
  </div>
  <div class="abs" style="left:253px;top:75px">
    <div class="contact-line"><svg width="6" height="6" viewBox="0 0 6 6"><path d="M1 0.5l1.2 0 .5 1.4-.7.6a3.5 3.5 0 0 0 1.5 1.5l.6-.7 1.4.5v1.2A4.6 4.6 0 0 1 1 0.5z" fill="var(--orange)"/></svg>+41 (0)41 555 01 23</div>
    <div class="contact-line"><svg width="6" height="6" viewBox="0 0 6 6"><rect x="1.5" y="0" width="3" height="6" rx=".5" fill="var(--orange)"/></svg>+41 (0)79 555 04 56 Mobile</div>
    <div class="contact-line"><svg width="6" height="6" viewBox="0 0 6 6"><rect x="0" y="1" width="6" height="4" fill="var(--orange)"/><path d="M0 1l3 2 3-2" stroke="#fff" stroke-width=".5" fill="none"/></svg>info@bernertreuhand.ch</div>
  </div>
  <div class="addr abs" style="left:20px;top:118px">
    <h3>LUZERN</h3>
    <p>Berner Treuhand Consulting GmbH<br>Haldenstrasse 12<br>6006 Luzern</p>
  </div>
  <div class="addr abs" style="left:253px;top:114px">
    <h3>ZÜRICH</h3>
    <p>Berner Treuhand Consulting GmbH<br>Seestrasse 80<br>8810 Horgen</p>
  </div>
  <div class="map" style="left:20px" role="img" aria-label="Anfahrtskarte Standort Luzern"></div>
  <div class="map" style="left:253px" role="img" aria-label="Anfahrtskarte Standort Horgen"></div>
</section>

</body>
</html>
```